依頼詳細
概要、特徴にも書いたように、今回、分離発注に向けた営業用のチラシを作成して頂きたいです。

・すでに既存で新規顧客獲得用のパンフレット(高難度松浦工業)とチラシ(HARUKAZE)があり、今回は、それらに追加で挟む “分離発注を目的としたチラシ” の依頼となります。

※既存(高難度パンフレット)(添付資料1、2)
+
既存(HARUKAZE)(添付資料3)
+
“分離発注を目的としたチラシ”

既存の3つのチラシ(※添付資料1.2.3)と一緒に挟んで、配布したいので

流れを理解して作成していただけたら幸いです。

・流れ、
株式会社松浦工業は、高難度の足場を専門で営業しています。

また、その職人で構成されている、HARUKAZEというワンランク上の足場サービスも運営しています。(住人さんや近隣様、などへの配慮、最高のサービスを提供するブランド)
(HARUKAZEにもホームページがございます。)

安全には、費用がかかります。
人の命は尊いです。
工事は足場から始まり、足場で終わります。
そして、業者みんなが使う足場です。

弊社の売りを武器として運営し維持して行くためには、無駄な予算を削り、その予算を安心できる工事に生かす。

そして見た目も美しい職人で揃えている私たちと手を組みませんか。

。。。といった流れでイメージして作成して頂きたいです。

※弊社の売りに関しましては、添付した資料やホームページを確認して頂き、理解して頂きたいです。

・目的は、新規顧客の獲得ですが、分離発注の提案を載せたいです。

・新規顧客(ターゲット)→ビル建物のオーナー、元請業社、ゼネコンなど

・メリットとデメリットをまとめたマインドマップも添付しますので、必要であれば使ってください。
・他にも、ホームページもありますので、見ていただけたら、と思います。
・弊社は改修工事用の足場をメインで運営しております。
(居住者様や、近隣様、歩行者様からの安心や業者間、現場管理監督様とのコミュニケーションもとても大切にしております。)
・メリットのマインドマップの他にも、弊社を使うことでのメリットは、たくさんあります。
・どの立場から見ても美しい足場屋を目指しております。

記載項目
分離発注しませんか。

株式会社松浦工業
042−718−2964
https://matsuurakogyo-ashiba.example
↑↑
株式会社松浦工業(高難度専門の足場サービス)

https://harukaze-ashiba.example
↑↑
ワンランク上の足場サービス
HARUKAZE ホームページ

サイズ
A4
ページ数
両面
希望イメージ
シンプル 複雑
単色 カラフル
暗い 明るい
日常 高級
遊び心 厳粛
未来的 伝統的
女性的 男性的
希望する色
黄・オレンジ系、緑系、青系、既存チラシ(添付資料1.2.3)とのバランスで決めて頂きたい
納品ファイル
• 高解像度JPG (.jpg)
• イラストレーター形式 (.ai)
補足説明
↑↑
株式会社松浦工業(高難度専門の足場サービス)

↑↑
ワンランク上の足場サービス
HARUKAZE ホームページ

どちらも並行して運営しております!

ーーーーーーーーーーーーーーーーーーーーーーーーー

※多少の文字の変更などがしやすいように、アウトライン化されていないデータでも納品して頂きたいです。
みなさま、すばらしい作品をありがとうございます!

みなさまの作品を見て間違えに気づくことが出来ました。

一部、変更させてください!

3点あるのですが、

①1つ目は、このチラシを誰に当てた手紙にするのか、ですが、ターゲットは、
・ビルやマンション、学校など建物のオーナー様
・ビルやマンションの管理をしている管理会社様や、
・不動産会社様
・店舗、等の工事担当者様
に当てた手紙で作成して頂きたいです。

※よく考えたら工事会社が直接足場屋に依頼するのは、当前のことだと思いましたので、工事業者に当てるのはおかしい話だと気付いたので宜しくお願いいたします。

②見積もり依頼までの流れを盛り込んで頂きたいです。
流れ
平日の9:00〜17:00に
042−718−2964

に電話をして頂き、弊社の電話に出た物に、見積もりして欲しい物件のご住所をお聞かせください。

or

当社ホームページ問い合わせフォームのQRコード?
かURL??

で見積もり依頼のメッセージを頂けたら、

1週間以内にTerravue Mapsを元に概算でお見積もりして郵送させて頂きます。

※建物の改修工事が決まりましたら、弊社と工事業者様とで直接お打ち合わせして、施工します!
※安心、安全へのクオリティは、高品質をお約束しますので、安心してください。
※足場工事は、命の危険を伴う工事です。

。。。のような感じをうまく刺さる形で表現して頂きたいです。

③ターゲットに分離発注という意味を理解してもらえるのかも不安になってきたのですが、どうでしょうか。

このチラシに足場だけを分離発注しませんか?なのか、
直接発注しませんか、なのか、何か良い表現があればそれも考えていただけると幸いです。

分離発注でわかるから大丈夫だよ、であれば分離発注も構いません。
ただ僕が不安になっただけなので、
そこも何か良い案があればなーと思ったので、宜しくお願いいたします。

コロナで、大ダメージを受けてしまったので、これで、復活したいと考えております!

みなさま、どうか宜しくお願いいたします!

弊社の既存のパンフレットと一緒に配ることを踏まえてこの作品が一番良いのではないかと感じました。

この度は、本当にありがとうございました。
僕たちは、職人さん達の生活がもっと潤っていけるように、したいと考えております。
職人さん達の世界では土曜も仕事をすることが当たり前となっております。
しかし僕たちは価値の高い仕事を社会に広めていき、みんなが、より良い工事をしながら、生活も潤っていけるように考えております。
皆さんが作ってくれた作品から、僕たちは大きな気づきをゲットしました!
とても感謝しています。
本当に本当にありがとうございました。

```html
<!DOCTYPE html>
<html lang="ja">
<head>
<meta charset="UTF-8">
<title>真心を込めるという誇り。 | 株式会社松浦工業</title>
<link rel="stylesheet" href="https://fonts.googleapis.com/css2?family=Klee+One:wght@600&family=M+PLUS+Rounded+1c:wght@700;800&family=Noto+Serif+JP:wght@700&display=swap">
<style>
  :root {
    --sky-top: #0b1d5c;
    --sky-mid: #1d4fb0;
    --sky-glow: #6fa6e6;
    --ground: #05081a;
    --band: #141d6b;
    --band-edge: #5d6fd6;
    --gold: #f5d21f;
    --white: #ffffff;
    --seal-red: #d8262f;
  }
  * { margin: 0; padding: 0; box-sizing: border-box; }
  html, body { width: 846px; height: 1200px; overflow: hidden; background: var(--ground); }
  .flyer {
    position: relative;
    width: 846px;
    height: 1200px;
    overflow: hidden;
    font-family: "M PLUS Rounded 1c", sans-serif;
    color: var(--white);
  }
  .scene-photo {
    position: absolute;
    inset: 0;
    background:
      radial-gradient(ellipse 70% 25% at 55% 76%, var(--sky-glow) 0%, rgba(111,166,230,0) 70%),
      linear-gradient(180deg, var(--sky-top) 0%, var(--sky-mid) 55%, #3a74cf 72%, #10205a 86%, var(--ground) 100%);
  }
  .tagline {
    position: absolute;
    top: 62px;
    right: 80px;
    writing-mode: vertical-rl;
    font-family: "Klee One", cursive;
    font-weight: 600;
    line-height: 1.55;
    letter-spacing: 0.02em;
  }
  .tagline-line { display: block; font-size: 84px; }
  .tagline-line.second { padding-top: 96px; }
  .tagline-accent { color: var(--gold); font-size: 112px; }
  .offer-band {
    position: absolute;
    left: 120px;
    right: 0;
    top: 790px;
    height: 185px;
    background: var(--band);
    border-top: 3px solid var(--band-edge);
    border-bottom: 3px solid var(--band-edge);
    border-left: 3px solid var(--band-edge);
  }
  .offer-lead {
    position: absolute;
    left: 28px;
    top: 26px;
    font-size: 40px;
    font-weight: 700;
    letter-spacing: 0.04em;
  }
  .value-badges {
    position: absolute;
    right: 20px;
    top: 16px;
    display: flex;
    gap: 12px;
  }
  .value-badge {
    width: 100px;
    height: 58px;
    border-radius: 28px;
    background: var(--white);
    color: var(--seal-red);
    font-size: 28px;
    font-weight: 800;
    display: flex;
    align-items: center;
    justify-content: center;
  }
  .offer-headline {
    position: absolute;
    left: 24px;
    top: 92px;
    font-weight: 800;
    white-space: nowrap;
    letter-spacing: 0.03em;
  }
  .offer-headline .key { color: var(--gold); font-size: 78px; }
  .offer-headline .rest { font-size: 58px; }
  .company-name {
    position: absolute;
    right: 60px;
    bottom: 32px;
    font-family: "Noto Serif JP", serif;
    font-weight: 700;
    font-size: 30px;
    letter-spacing: 0.06em;
  }
</style>
</head>
<body>
  <main class="flyer">
    <div class="scene-photo" role="img" aria-label="青い夕空を背景に、改修工事の足場の上で作業する職人たちのシルエット写真"></div>

    <h1 class="tagline">
      <span class="tagline-line"><span class="tagline-accent">真心</span>を込める</span>
      <span class="tagline-line second">という誇り。</span>
    </h1>

    <section class="offer-band">
      <p class="offer-lead">改修工事用足場の</p>
      <ul class="value-badges" style="list-style:none">
        <li class="value-badge">安心</li>
        <li class="value-badge">安全</li>
        <li class="value-badge">信頼</li>
      </ul>
      <p class="offer-headline"><span class="key">直接依頼</span><span class="rest">承ります！</span></p>
    </section>

    <p class="company-name">株式会社松浦工業</p>
  </main>
</body>
</html>
```